'Marlow Ridge' wine label

We are looking to create a new wine brand called "Marlow Ridge."

We have no preconceived notions about color, design or otherwise. This design should be incorporated into a wine label that will ultimately be affixed to either a 750ml bottle or a wine box. We've attached some images of wine label artwork and bottle shots - but yours does NOT need to look like these - they're there just for illustration purposes.

Target Market(s)

Target market for this wine brand will be "broad market" retail - i.e., big box stores, wine shops, etc.

Logo Text

Marlow Ridge

```html
<!DOCTYPE html>
<html lang="en">
<head>
<meta charset="utf-8">
<title>Marlow Ridge — Wine Label</title>
<link rel="stylesheet" href="https://fonts.googleapis.com/css2?family=Cinzel:wght@400;500&family=Berkshire+Swash&display=swap">
<style>
  :root {
    --purple-deep: #5e0a86;
    --purple-main: #8414a8;
    --purple-band: #4c0868;
    --berry: #b8305f;
    --berry-line: #a2124f;
    --lilac: #b27fcb;
    --ink: #0c0010;
    --white: #ffffff;
    --wine-dark: #2a0014;
    --wine-bright: #c2124e;
  }
  html, body {
    margin: 0;
    padding: 0;
    width: 1200px;
    height: 981px;
    overflow: hidden;
    background: #ffffff;
  }
  .label {
    position: relative;
    width: 1200px;
    height: 981px;
    box-sizing: border-box;
    border: 2px solid var(--ink);
    overflow: hidden;
    background: linear-gradient(100deg, var(--purple-deep) 0%, var(--purple-main) 45%, #9a1da8 70%, var(--berry) 100%);
  }
  .label__vine-pattern {
    position: absolute;
    inset: 0;
    background:
      radial-gradient(ellipse 260px 220px at 150px 120px, rgba(190,120,220,0.16), transparent 70%),
      radial-gradient(ellipse 240px 220px at 160px 620px, rgba(190,120,220,0.14), transparent 70%),
      radial-gradient(ellipse 240px 220px at 540px 820px, rgba(190,120,220,0.12), transparent 70%),
      radial-gradient(ellipse 220px 200px at 520px 120px, rgba(190,120,220,0.12), transparent 70%);
  }
  .label__grapes {
    position: absolute;
    top: 0;
    right: 0;
    width: 400px;
    height: 100%;
    background:
      radial-gradient(circle 110px at 300px 110px, rgba(230,90,120,0.55), transparent 75%),
      radial-gradient(circle 120px at 330px 330px, rgba(220,40,80,0.55), transparent 75%),
      radial-gradient(circle 110px at 260px 560px, rgba(220,60,100,0.45), transparent 75%),
      radial-gradient(circle 120px at 330px 720px, rgba(210,60,100,0.45), transparent 75%),
      linear-gradient(90deg, rgba(184,48,95,0) 0%, rgba(184,48,95,0.6) 45%, rgba(190,50,90,0.75) 100%);
  }
  .label__band {
    position: absolute;
    left: 0;
    top: 172px;
    width: 100%;
    height: 278px;
    box-sizing: border-box;
    border-top: 5px solid var(--berry-line);
    border-bottom: 5px solid var(--berry-line);
    background: linear-gradient(90deg, rgba(70,6,98,0.85) 0%, rgba(80,8,104,0.8) 60%, rgba(120,20,90,0.35) 100%);
  }
  .label__title {
    position: absolute;
    inset: 0;
    width: 1200px;
    height: 981px;
  }
  .title__surname {
    font-family: "Cinzel", "Trajan Pro", serif;
    font-weight: 400;
    font-size: 290px;
  }
  .title__given {
    font-family: "Berkshire Swash", cursive;
    font-size: 168px;
  }
  .title__vintage {
    font-family: "Cinzel", serif;
    font-size: 50px;
    letter-spacing: 6px;
  }
  .label__region {
    position: absolute;
    left: 0;
    top: 837px;
    width: 100%;
    height: 56px;
    background: linear-gradient(90deg, var(--wine-dark) 0%, #6a0032 35%, var(--wine-bright) 70%, #8e0a3a 100%);
    display: flex;
    align-items: center;
    justify-content: center;
  }
  .region__name {
    font-family: "Cinzel", serif;
    font-size: 38px;
    letter-spacing: 6px;
    color: var(--white);
    margin: 0;
    padding-left: 8px;
  }
</style>
</head>
<body>
  <main class="label">
    <div class="label__vine-pattern" role="img" aria-label="Faint grape-leaf vine pattern across the background"></div>
    <div class="label__grapes" role="img" aria-label="Close-up photograph of red grapes along the right edge"></div>
    <div class="label__band"></div>

    <svg class="label__title" viewBox="0 0 1200 981" xmlns="http://www.w3.org/2000/svg" aria-label="Marlow Ridge 2008">
      <g class="title__surname">
        <text x="60" y="402" textLength="1090" lengthAdjust="spacingAndGlyphs" fill="#0c0010">MARLOW</text>
        <text x="54" y="396" textLength="1090" lengthAdjust="spacingAndGlyphs" fill="#b27fcb">MARLOW</text>
      </g>
      <g class="title__given" text-anchor="middle">
        <text x="678" y="594" fill="#0c0010">Ridge</text>
        <text x="672" y="588" fill="#ffffff">Ridge</text>
      </g>
      <text class="title__vintage" x="762" y="690" text-anchor="middle" fill="#ffffff">2008</text>
    </svg>

    <div class="label__region">
      <p class="region__name">CALIFORNIA</p>
    </div>
  </main>
</body>
</html>
```